New Business Card Design Project

We are looking for a talented individual to create a truly awesome/unique business card design for us. We are looking for a someone to design something that will really stand out from the crowd - we don't mind what ideas you come up with (ie embossed/flat/matte/shine etc etc) just wow us with your creativity.
Updates

Sick

Target Market(s)

Video Games Industry Professionals (all levels of seniority from QA Testers through to CEOs)

Contact Information for Business Card

Company logo (see upload)
Company name: Northbridge Play Careers Ltd
Employee Name: Harriet Vasko
Job title: CEO
Website: www.npc2go.com
Office +44 1632 960418
Mobile: +44 7700 900582
Email: harriet@npc2go.com

Colors

Designer to choose colors to be used in the design.

Requirements
Must have
• The business card design MUST contain all the information listed in the BUSINESS CARD DETAILS box.
• You will see the colours that are relevant to us (ie company logo) in the uploaded imagery - however you do not have to use all these colours when designing the business card itself
• MUST BE DOUBLE SIDED

```html
<!DOCTYPE html>
<html lang="en">
<head>
<meta charset="utf-8">
<title>Northbridge Play Careers – Business Card</title>
<link href="https://fonts.googleapis.com/css2?family=Montserrat:wght@500;600;700;800&display=swap" rel="stylesheet">
<style>
  :root {
    --backdrop: #4a4a4a;
    --card-dark: #3c3c3c;
    --card-light: #ffffff;
    --navy: #1d2d5c;
    --orange: #f47b20;
    --ink: #1a1a1a;
  }
  * { box-sizing: border-box; margin: 0; padding: 0; }
  html, body { width: 1200px; height: 1000px; overflow: hidden; }
  body {
    background: var(--backdrop);
    font-family: "Montserrat", Arial, sans-serif;
    position: relative;
  }
  .card {
    position: absolute;
    left: 280px;
    width: 640px;
    height: 366px;
    border-radius: 24px;
    overflow: hidden;
    box-shadow: 0 10px 30px rgba(0,0,0,0.35);
  }
  .card-back { top: 70px; background: var(--card-dark); }
  .card-front { top: 540px; background: var(--card-light); }

  .brand {
    position: absolute;
    top: 50%;
    left: 50%;
    transform: translate(-50%, -50%);
    display: flex;
    align-items: center;
    gap: 26px;
  }
  .brand-mark {
    width: 120px; height: 120px;
    border-radius: 50%;
    background: var(--navy);
    flex: none;
  }
  .brand-name {
    font-weight: 800;
    font-size: 34px;
    line-height: 1.15;
    color: #ffffff;
    width: 300px;
  }

  .front-mark {
    position: absolute;
    left: 70px; top: 92px;
    width: 150px; height: 150px;
    border-radius: 50%;
    background: var(--navy);
  }
  .divider {
    position: absolute;
    left: 262px; top: 100px;
    width: 2px; height: 160px;
    background: var(--orange);
  }
  .person {
    position: absolute;
    left: 282px; top: 98px;
  }
  .person-name {
    font-weight: 700;
    font-size: 28px;
    color: var(--navy);
    line-height: 1.1;
  }
  .person-title {
    font-weight: 500;
    font-size: 15px;
    color: var(--orange);
    margin-top: 2px;
  }
  .contacts {
    list-style: none;
    margin-top: 16px;
  }
  .contacts li {
    display: flex;
    align-items: center;
    gap: 10px;
    font-weight: 600;
    font-size: 16px;
    color: var(--ink);
    height: 24px;
  }
  .contacts svg { width: 13px; height: 13px; flex: none; }
  .accent { color: var(--orange); }
  .wave { position: absolute; inset: 0; width: 100%; height: 100%; }
</style>
</head>
<body>

<section class="card card-back" aria-label="Card back">
  <div class="brand">
    <span class="brand-mark" aria-hidden="true"></span>
    <span class="brand-name">Northbridge Play Careers</span>
  </div>
</section>

<section class="card card-front" aria-label="Card front">
  <svg class="wave" viewBox="0 0 640 366" preserveAspectRatio="none" aria-hidden="true">
    <path fill="var(--orange)" d="M0,242 C150,240 255,286 380,320 C260,300 150,254 0,256 Z"/>
    <path fill="var(--orange)" d="M380,320 C480,334 560,322 640,312 L640,328 C560,336 470,336 380,320 Z"/>
    <path fill="var(--navy)" stroke="#ffffff" stroke-width="2" d="M0,260 C150,256 260,302 380,322 C470,338 560,338 640,332 L640,366 L0,366 Z"/>
  </svg>

  <span class="front-mark" role="img" aria-label="Company mark"></span>
  <span class="divider" aria-hidden="true"></span>

  <div class="person">
    <h1 class="person-name">Harriet Vasko</h1>
    <p class="person-title">CEO</p>
    <ul class="contacts">
      <li>
        <svg viewBox="0 0 24 24" aria-hidden="true"><path fill="var(--orange)" d="M6.6 10.8a15 15 0 0 0 6.6 6.6l2.2-2.2a1 1 0 0 1 1-.25 11.4 11.4 0 0 0 3.6.57 1 1 0 0 1 1 1V20a1 1 0 0 1-1 1A17 17 0 0 1 3 4a1 1 0 0 1 1-1h3.5a1 1 0 0 1 1 1c0 1.25.2 2.45.57 3.6a1 1 0 0 1-.25 1z"/></svg>
        +44 1632 960418
      </li>
      <li>
        <svg viewBox="0 0 24 24" aria-hidden="true"><rect x="6" y="2" width="12" height="20" rx="2" fill="none" stroke="var(--orange)" stroke-width="2"/><circle cx="12" cy="18" r="1.2" fill="var(--orange)"/></svg>
        +44 7700 900582
      </li>
      <li>
        <svg viewBox="0 0 24 24" aria-hidden="true"><rect x="2" y="5" width="20" height="14" rx="2" fill="var(--orange)"/><path d="M3 6l9 7 9-7" fill="none" stroke="#fff" stroke-width="1.6"/></svg>
        harriet@npc2go.com
      </li>
      <li>
        <svg viewBox="0 0 24 24" aria-hidden="true"><circle cx="12" cy="12" r="10" fill="var(--orange)"/><path d="M2 12h20M12 2c3 3 3 17 0 20M12 2c-3 3-3 17 0 20" fill="none" stroke="#fff" stroke-width="1.4"/></svg>
        <span>www.<span class="accent">npc2go</span>.com</span>
      </li>
    </ul>
  </div>
</section>

</body>
</html>
```